Company Website for an IT business called "BRIGHT HARBOR"

Complete website creation with text and graphics.
We need :
- modern and creative design for our IT company
- Content management system to edit text later on
- Integrate third party content from partner company
- Contact form (transfer by email)
Updates

Target Market(s)

Small and medium business
private customers

Industry/Entity Type

Information Technology

Coding

Coded - Design and coding required

Number of Pages Required

1 page

Font styles to use
Sans Serif

Requirements
Must have
• Contact form
Link to legal information
Link to data protection (GDPR)
Link to website owner declaration
Nice to have
• Fresh and creative graphics for IT business

```html
<!DOCTYPE html>
<html lang="en">
<head>
<meta charset="utf-8">
<title>Bright Harbor — IT Services</title>
<link href="https://fonts.googleapis.com/css2?family=Montserrat:wght@400;500;600;700;800&family=Poppins:wght@300;400;500;600;700&display=swap" rel="stylesheet">
<style>
:root{
  --blue:#0f8fd8;
  --blue-bright:#1aa3ec;
  --navy:#141c2e;
  --navy-deep:#1a1f4d;
  --ink:#1d2330;
  --text:#5c6470;
  --pale:#f3f7fb;
  --mist:#e4edf5;
  --white:#ffffff;
}
*{margin:0;padding:0;box-sizing:border-box}
html,body{width:1200px;height:4208px;overflow:hidden}
body{position:relative;font-family:"Montserrat",sans-serif;color:var(--ink);background:var(--white)}
.abs{position:absolute}
a{color:inherit;text-decoration:none}

/* header */
.site-header{left:0;top:0;width:1200px;height:74px;background:var(--white)}
.brand{left:150px;top:18px;font-family:"Montserrat",sans-serif;font-weight:600;font-size:19px;letter-spacing:2px;color:var(--ink);display:flex;align-items:center;gap:10px;height:38px}
.brand-dot{width:14px;height:14px;border-radius:50%;background:var(--blue)}
.main-nav{top:28px;left:0;font-size:15px;color:#555}
.main-nav a{position:absolute;white-space:nowrap;top:0}
.main-nav .active{color:var(--ink);font-weight:600;border-bottom:2px solid var(--blue);padding-bottom:8px}

/* hero */
.hero{left:0;top:74px;width:1200px;height:628px}
.hero-title{left:148px;top:170px;font-family:"Poppins",sans-serif;font-weight:700;font-size:50px;line-height:58px;color:var(--white)}
.hero-sub{left:148px;top:300px;font-family:"Poppins",sans-serif;font-size:17px;color:var(--white)}
.btn{display:flex;align-items:center;justify-content:center;font-size:11px;font-weight:700;letter-spacing:.4px;text-transform:uppercase}
.btn-light{left:148px;top:356px;width:130px;height:36px;background:var(--white);color:var(--ink);border-radius:2px}
.btn-blue{background:var(--blue);color:var(--white);border-radius:2px}

/* about */
.eyebrow{font-size:19px;color:var(--blue);font-weight:500}
.about-title{left:150px;top:832px;width:450px;font-size:25px;line-height:39px;font-weight:800;color:var(--ink);text-transform:uppercase}
.about-copy{left:150px;top:918px;width:445px;font-size:12.5px;line-height:24.5px;color:var(--text)}

/* sections headings */
.section-title{left:0;width:1200px;text-align:center;font-size:32px;font-weight:400;letter-spacing:-.3px}
.section-title strong{font-weight:800}
.rule{width:64px;height:3px;background:var(--blue);left:568px}

/* services */
.service{width:260px;text-align:center;color:var(--white)}
.service h3{font-size:14.5px;font-weight:700;margin-top:10px;text-transform:uppercase}
.service p{font-size:12.5px;line-height:18px;color:#b7bfcc;margin-top:6px}
.service a{display:inline-block;margin-top:12px;font-size:11.5px;color:var(--blue-bright);text-decoration:underline}
.service svg{display:block;margin:0 auto}
.panel{left:760px;top:1590px;width:274px;height:215px;background:rgba(30,60,90,.65)}

/* why */
.why-intro{left:320px;top:2343px;width:560px;text-align:center;font-size:13.5px;line-height:22px;color:var(--text)}
.reason{width:200px;text-align:center}
.reason h3{font-size:21px;font-weight:600;margin-top:4px}
.reason p{font-size:12px;line-height:16.5px;color:var(--text);margin-top:4px}
.reason svg{display:block;margin:0 auto}

/* security */
.security-title{left:715px;top:2968px;font-size:35px;line-height:46px;font-weight:400;color:var(--ink)}
.security-title strong{color:var(--blue);font-weight:700}
.security-copy{left:715px;top:3072px;width:345px;font-size:12px;line-height:24px;color:var(--text)}

/* contact */
.contact-title{left:148px;top:3440px;font-size:30px;color:var(--white);font-weight:400}
.contact-title strong{font-weight:800}
.field{background:rgba(255,255,255,.72);border:1px solid rgba(255,255,255,.9);border-radius:3px;font-size:12px;color:#6b7480;padding:10px 15px}

/* footer */
.footer-brand{left:180px;top:3910px;font-size:25px;font-weight:600;letter-spacing:3px;color:var(--ink);display:flex;align-items:center;gap:12px}
.footer-info{font-size:13px;color:#444;display:flex;gap:10px;align-items:flex-start;line-height:20px}
.footer-head{font-size:16px;font-weight:600;text-transform:uppercase;color:var(--ink)}
.footer-links{left:486px;top:3930px;list-style:none;font-size:12.5px;color:#333;line-height:25.5px}
.footer-links li::before{content:"›";margin-right:8px;font-size:15px}
.social{width:37px;height:37px;border-radius:50%;background:var(--blue)}
.legal-bar{left:0;top:4130px;width:1200px;height:1px;background:#dde3ea}
.copyright{left:182px;top:4158px;font-size:12px;color:#444}
.legal-links{left:864px;top:4158px;font-size:12px;color:#444}
</style>
</head>
<body>

<header class="site-header abs">
  <div class="brand abs"><span class="brand-dot"></span>BRIGHT HARBOR</div>
  <nav class="main-nav abs">
    <a class="active" style="left:573px">Home</a>
    <a style="left:655px">About</a>
    <a style="left:738px">Services</a>
    <a style="left:838px">Data Protection</a>
    <a style="left:989px">Contact</a>
  </nav>
</header>

<section class="hero abs">
  <svg class="abs" width="1200" height="628" style="left:0;top:0">
    <defs>
      <linearGradient id="heroPhoto" x1="0" y1="0" x2="1" y2="1">
        <stop offset="0" stop-color="#3d9bd8"/><stop offset="1" stop-color="#1a7cc4"/>
      </linearGradient>
      <linearGradient id="heroData" x1="0" y1="0" x2="0" y2="1">
        <stop offset="0" stop-color="#1b1f55"/><stop offset=".6" stop-color="#16376f"/><stop offset="1" stop-color="#0f6aa8"/>
      </linearGradient>
    </defs>
    <rect width="1200" height="628" fill="url(#heroPhoto)" role="img" aria-label="Photo of a team working together at laptops in an office, tinted blue"/>
    <polygon points="670,0 1200,0 1200,628 416,628" fill="url(#heroData)" role="img" aria-label="Illustration of glowing blue data points rising like a city skyline"/>
  </svg>
  <h1 class="hero-title abs">Data<br>Protection</h1>
  <p class="hero-sub abs">Lorem Ipsum is simply dummy text.</p>
  <a class="btn btn-light abs">Read More</a>
</section>

<section class="about">
  <p class="eyebrow abs" style="left:150px;top:800px">About Us</p>
  <h2 class="about-title abs">Lorem Ipsum is simply dummy text of the printing</h2>
  <p class="about-copy abs">Lorem Ipsum is simply dummy text of the printing and typesetting industry. Lorem Ipsum has been the industry's standard dummy text ever since the 1500s, when an unknown printer took a galley of type and scrambled it to make a type specimen book. It has survived not only five centuries, but also the leap into electronic typesetting, remaining essentially unchanged.</p>
  <a class="btn btn-blue abs" style="left:150px;top:1091px;width:130px;height:36px">Read More</a>
  <svg class="abs" width="320" height="390" style="left:690px;top:772px" role="img" aria-label="Photo of people at work with laptops and papers">
    <defs><linearGradient id="aboutPhoto" x1="0" y1="0" x2="1" y2="1"><stop offset="0" stop-color="#c9b7a6"/><stop offset="1" stop-color="#5b5f66"/></linearGradient></defs>
    <polygon points="30,110 150,110 150,390 30,390" fill="url(#aboutPhoto)" opacity=".0"/>
    <polygon points="130,0 300,0 300,275 90,275" fill="url(#aboutPhoto)" opacity=".9"/>
  </svg>
</section>

<section class="provide">
  <svg class="abs" width="1200" height="1080" style="left:0;top:1188px">
    <defs><linearGradient id="darkBg" x1="0" y1="0" x2="1" y2="1"><stop offset="0" stop-color="#151a27"/><stop offset="1" stop-color="#1d2637"/></linearGradient></defs>
    <polygon points="0,110 1200,0 1200,1010 0,1070" fill="url(#darkBg)" role="img" aria-label="Dark background photo of a person using technology"/>
    <polygon points="0,110 1200,0 1200,18 0,124" fill="var(--blue)"/>
    <polygon points="0,1054 1200,945 1200,958 0,1072" fill="var(--blue)"/>
    <polygon points="0,1072 1200,958 1200,1080 0,1080" fill="var(--pale)"/>
  </svg>
  <h2 class="section-title abs" style="top:1350px;color:var(--white)">WHAT <strong>WE PROVIDE</strong></h2>
  <div class="rule abs" style="top:1400px"></div>
  <div class="panel abs"></div>

  <div class="service abs" style="left:392px;top:1448px">
    <svg width="70" height="62" viewBox="0 0 70 62" fill="none" stroke="#fff" stroke-width="2"><path d="M22 26a10 10 0 0 1 4-18 13 13 0 0 1 24 3 8 8 0 0 1 2 15z"/><rect x="10" y="34" width="14" height="22" rx="2"/><path d="M28 50h20l8-8"/></svg>
    <h3>Data Protection</h3><p>Lorem Ipsum is simply dummy text<br>of the printing and typesetting.</p><a>LEARN MORE</a>
  </div>
  <div class="service abs" style="left:751px;top:1610px">
    <svg width="66" height="62" viewBox="0 0 66 62" fill="none" stroke="var(--blue-bright)" stroke-width="2"><path d="M33 24 22 13a6 6 0 0 1 11-7 6 6 0 0 1 11 7z"/><circle cx="14" cy="42" r="5"/><circle cx="33" cy="42" r="5"/><circle cx="52" cy="42" r="5"/><path d="M5 60a9 9 0 0 1 18 0M24 60a9 9 0 0 1 18 0M43 60a9 9 0 0 1 18 0M33 24v12"/></svg>
    <h3>Customer Satisfaction</h3><p>Lorem Ipsum is simply dummy text<br>of the printing and typesetting.</p><a>LEARN MORE</a>
  </div>
  <div class="service abs" style="left:186px;top:1744px">
    <svg width="70" height="64" viewBox="0 0 70 64" fill="none" stroke="#fff" stroke-width="2"><rect x="20" y="4" width="30" height="18" rx="2"/><path d="M10 30h50M16 30v30M54 30v30M26 30v18h18V30M28 54h14"/></svg>
    <h3>IT Consulting</h3><p>Lorem Ipsum is simply dummy text<br>of the printing and typesetting.</p><a>LEARN MORE</a>
  </div>
  <div class="service abs" style="left:520px;top:1920px">
    <svg width="50" height="62" viewBox="0 0 50 62" fill="none" stroke="#fff" stroke-width="2"><rect x="6" y="4" width="38" height="50" rx="2"/><path d="M25 14v20M15 20h20M12 30l4-8 4 8zM30 30l4-8 4 8zM18 42h14"/></svg>
    <h3>Legal Information</h3><p>Lorem Ipsum is simply dummy text<br>of the printing and typesetting.</p><a>LEARN MORE</a>
  </div>
</section>

<section class="why">
  <div class="abs" style="left:0;top:2268px;width:1200px;height:584px;background:var(--pale)"></div>
  <h2 class="section-title abs" style="top:2270px;color:var(--ink)">WHY <strong>CHOSE US</strong></h2>
  <div class="rule abs" style="top:2320px"></div>
  <p class="why-intro abs">Lorem Ipsum is simply dummy text of the printing and typesetting industry. Lorem Ipsum has been the industry's standard dummy text .</p>

  <div class="reason abs" style="left:860px;top:2402px">
    <svg width="50" height="50" viewBox="0 0 50 50" fill="none" stroke="#333" stroke-width="2"><circle cx="25" cy="22" r="14"/><circle cx="25" cy="22" r="8"/><circle cx="25" cy="22" r="2"/><path d="M10 48h30M25 36v12"/></svg>
    <h3>Support</h3><p>Lorem ipsum dolor sit amet,<br>consectetur adipisicing elit, sed<br>do eiusmod tempor</p>
    <svg width="34" height="34" viewBox="0 0 34 34" fill="none" stroke="var(--blue)" stroke-width="2" style="margin-top:10px"><circle cx="17" cy="17" r="15"/><path d="m11 14 6 6 6-6"/></svg>
  </div>
  <div class="reason abs" style="left:500px;top:2484px">
    <svg width="50" height="50" viewBox="0 0 50 50" fill="none" stroke="#333" stroke-width="2"><circle cx="25" cy="22" r="14"/><circle cx="25" cy="22" r="8"/><circle cx="25" cy="22" r="2"/><path d="M10 48h30M25 36v12"/></svg>
    <h3>Support</h3><p>Lorem ipsum dolor sit amet,<br>consectetur adipisicing elit, sed<br>do eiusmod tempor</p>
    <svg width="34" height="34" viewBox="0 0 34 34" fill="none" stroke="var(--blue)" stroke-width="2" style="margin-top:10px"><circle cx="17" cy="17" r="15"/><path d="m11 14 6 6 6-6"/></svg>
  </div>
  <div class="reason abs" style="left:140px;top:2580px">
    <svg width="50" height="50" viewBox="0 0 50 50" fill="none" stroke="#333" stroke-width="2"><circle cx="25" cy="22" r="14"/><circle cx="25" cy="22" r="8"/><circle cx="25" cy="22" r="2"/><path d="M10 48h30M25 36v12"/></svg>
    <h3>Support</h3><p>Lorem ipsum dolor sit amet,<br>consectetur adipisicing elit, sed<br>do eiusmod tempor</p>
    <svg width="34" height="34" viewBox="0 0 34 34" fill="none" stroke="var(--blue)" stroke-width="2" style="margin-top:10px"><circle cx="17" cy="17" r="15"/><path d="m11 14 6 6 6-6"/></svg>
  </div>
</section>

<section class="security">
  <div class="abs" style="left:0;top:2852px;width:1200px;height:505px;background:var(--mist)"></div>
  <svg class="abs" width="540" height="325" style="left:150px;top:2940px" role="img" aria-label="Photo of hands typing on a laptop with a glowing security shield">
    <defs><linearGradient id="secPhoto" x1="0" y1="0" x2="1" y2="1"><stop offset="0" stop-color="#1b3a5c"/><stop offset=".6" stop-color="#2c6c9a"/><stop offset="1" stop-color="#c46a4e"/></linearGradient></defs>
    <polygon points="0,0 410,0 318,325 0,325" fill="url(#secPhoto)"/>
  </svg>
  <h2 class="security-title abs">Opting for <strong>Security</strong><br><strong>in the Future.</strong></h2>
  <p class="security-copy abs">Lorem Ipsum is simply dummy text of the printing and typesetting industry. Lorem Ipsum has been the industry's. Lorem Ipsum is simply dummy text of the printing.</p>
  <a class="btn btn-blue abs" style="left:715px;top:3172px;width:131px;height:37px">Support</a>
</section>

<section class="contact">
  <svg class="abs" width="1200" height="520" style="left:0;top:3356px" role="img" aria-label="Photo of a hand holding a smartphone, tinted bright blue">
    <defs><linearGradient id="contactBg" x1="0" y1="0" x2="1" y2="1"><stop offset="0" stop-color="#46b8e8"/><stop offset=".6" stop-color="#5fc6ee"/><stop offset="1" stop-color="#3aa6de"/></linearGradient></defs>
    <rect width="1200" height="520" fill="url(#contactBg)"/>
  </svg>
  <h2 class="contact-title abs">GET IN <strong>TOUCH</strong></h2>
  <div class="field abs" style="left:150px;top:3510px;width:256px;height:37px">Your Name</div>
  <div class="field abs" style="left:150px;top:3565px;width:256px;height:37px">Your Email</div>
  <div class="field abs" style="left:150px;top:3620px;width:256px;height:37px">Mobile</div>
  <div class="field abs" style="left:424px;top:3510px;width:284px;height:150px">Your Message</div>
  <a class="btn btn-blue abs" style="left:150px;top:3677px;width:108px;height:39px;font-size:14px;font-weight:500;text-transform:none">Submit</a>
</section>

<footer class="site-footer">
  <svg class="abs" width="1200" height="360" style="left:0;top:3790px">
    <path d="M0 80 C300 0 800 -10 1200 70 L1200 360 L0 360Z" fill="var(--blue)"/>
    <path d="M0 100 C350 30 800 40 1200 130 L1200 360 L0 360Z" fill="var(--white)"/>
  </svg>
  <div class="footer-brand abs"><span class="brand-dot"></span>BRIGHT HARBOR</div>
  <div class="footer-info abs" style="left:180px;top:3986px">
    <svg width="14" height="18" viewBox="0 0 14 18"><path d="M7 0a7 7 0 0 0-7 7c0 5 7 11 7 11s7-6 7-11a7 7 0 0 0-7-7z" fill="#333"/><circle cx="7" cy="7" r="2.5" fill="#fff"/></svg>
    <span>48 Harbor Lane Suite 5<br>Austin 78701 TX</span>
  </div>
  <div class="footer-info abs" style="left:180px;top:4046px;color:var(--blue);font-size:16px">
    <svg width="16" height="16" viewBox="0 0 24 24"><path d="M6.6 10.8a15 15 0 0 0 6.6 6.6l2.2-2.2a1 1 0 0 1 1-.25 11.4 11.4 0 0 0 3.6.57 1 1 0 0 1 1 1V20a1 1 0 0 1-1 1A17 17 0 0 1 3 4a1 1 0 0 1 1-1h3.5a1 1 0 0 1 1 1c0 1.25.2 2.45.57 3.57a1 1 0 0 1-.25 1z" fill="#333"/></svg>
    <span>(555) 014 2230</span>
  </div>
  <h3 class="footer-head abs" style="left:486px;top:3892px">Company</h3>
  <ul class="footer-links abs">
    <li>Home</li><li>About Us</li><li>Services</li><li>Data Protection</li><li>Contact Us</li>
  </ul>
  <h3 class="footer-head abs" style="left:694px;top:3892px">Follow Us</h3>
  <div class="social abs" style="left:694px;top:3958px" aria-label="Social profile"></div>
  <div class="social abs" style="left:738px;top:3958px" aria-label="Social profile"></div>
  <div class="social abs" style="left:781px;top:3958px" aria-label="Social profile"></div>
  <div class="social abs" style="left:826px;top:3958px" aria-label="Social profile"></div>
  <div class="legal-bar abs"></div>
  <p class="copyright abs">© 2021 Bright Harbor. All Rights Reserved.</p>
  <p class="legal-links abs"><a>Privacy Policy</a> | <a>Terms of Use</a></p>
</footer>

</body>
</html>
```